Harbor Lantern Podcast needs fun, creative cover art

Launching a new podcast called 'Opening Windows Toward Brighter Days' - aimed at an audience 30-50 who are interested in the practicalities of managing their money but also the more mental and emotional aspects.
Looking for something not too serious, warm and friendly.

Must be easy to read on phone screens
3000 x 3000 in size
Avoid currency symbols $, £ etc, as may have an international audience

Target Market(s)

Podcast listeners age 30-50 starting in the UK but then worldwide. Probably 60:40 female bias

Industry/Entity Type

Life Coaching

Font styles to use
Serif
Sans Serif

Colors
cadf82
fee18a
acd037
85cae6
eea4c8
f59195
85acd3

Requirements
Must have
• Simple, clear design. Easy to read on variety of devices. 3000 x 3000
Appeal to those with a spiritual or emotional interests
Nice to have
• Stand out among other money related podcasts
Maybe play around with clouds, lightbulbs and clearing skies
Should not have
• Currency symbols such as $ or £
Be too corporate or bank like
Stock images

```html
<!DOCTYPE html>
<html lang="en">
<head>
<meta charset="utf-8">
<title>Opening Windows Toward Brighter Days — Harbor Lantern Podcast</title>
<link rel="stylesheet" href="https://fonts.googleapis.com/css2?family=Delius&display=swap">
<style>
  :root {
    --navy-deep: #062f52;
    --navy: #0a4675;
    --navy-glow: #125a94;
    --sun-yellow: #f7dc0a;
    --cloud-white: #efeeea;
    --text-shadow: rgba(2, 20, 38, 0.6);
  }
  html, body {
    margin: 0;
    padding: 0;
    width: 1200px;
    height: 1200px;
    overflow: hidden;
    background: var(--navy-deep);
  }
  .cover {
    position: relative;
    width: 1200px;
    height: 1200px;
    overflow: hidden;
  }
  .sky-backdrop {
    position: absolute;
    inset: 0;
    background: radial-gradient(circle at 54% 46%, var(--navy-glow) 0%, var(--navy) 45%, var(--navy-deep) 100%);
  }
  .title {
    position: absolute;
    inset: 0;
    width: 1200px;
    height: 1200px;
    font-family: "Delius", "Comic Sans MS", sans-serif;
    font-weight: 400;
    filter: drop-shadow(4px 5px 0 var(--text-shadow));
  }
  .title-lead { font-size: 84px; fill: var(--cloud-white); }
  .title-accent { font-size: 260px; fill: var(--sun-yellow); }
  .title-side { font-size: 60px; fill: var(--sun-yellow); }
  .title-closing { font-size: 400px; fill: var(--cloud-white); }
</style>
</head>
<body>
  <main class="cover" aria-label="Harbor Lantern Podcast cover art">
    <div class="sky-backdrop" role="img" aria-label="Deep navy sky radiating soft light from the centre"></div>
    <svg class="title" viewBox="0 0 1200 1200" role="heading" aria-level="1" aria-label="Opening Windows Toward Brighter Days">
      <text class="title-lead" x="200" y="396" transform="rotate(-12.9 200 396)">opening windows</text>
      <text class="title-accent" x="185" y="660" transform="rotate(-12.5 185 660)">toward</text>
      <text class="title-side" x="1012" y="200" transform="rotate(90 1012 200)">brighter</text>
      <text class="title-closing" x="150" y="990" transform="rotate(-12.5 150 990)">days</text>
    </svg>
  </main>
</body>
</html>
```